4 x Florist Footpath Signage Boards that are consistant with each other for a modern florist

Eye catching, easy to read. little bit floral.
See example attached for wording. We are a modern florist in a country town.
This will be out on the street and needs to stand out!!

The Signage Panels
1. Valentines Day - 14th Feb
2. Workshop Signage boards - see attached example
3. Mothers Day Signage Board - 'Treat mum this Mothers Day'
4. We Are Open

Attached is a copy of the design guidelines and the template. the base of the sign is white.

Target Market(s)

Modern

Industry/Entity Type

Florist

Font styles to use
Sans Serif

Colors
eea4c8
f59296
ffffff
757575

Requirements
Must have
• flowers
• weddings
• giftware
• workshops
• flowers make people happy
• odettemarshpetals.co.nz
Nice to have
• Logo
• little bit of floral or greenery
• my shop is modem and industrial
Should not have
• Needs to be able to read easy

```html
<!DOCTYPE html>
<html lang="en">
<head>
<meta charset="utf-8">
<title>Odette Marsh Petals – Footpath Board</title>
<link rel="stylesheet" href="https://fonts.googleapis.com/css2?family=Roboto:wght@400;700&display=swap">
<style>
  :root {
    --board-white: #ffffff;
    --ink: #231f20;
    --leaf-deep: #7ea03e;
    --leaf-bright: #a9c23c;
    --leaf-pale: #dfe9c2;
  }
  html, body {
    margin: 0;
    padding: 0;
    width: 906px;
    height: 1200px;
    overflow: hidden;
    background: var(--board-white);
  }
  .board {
    position: relative;
    width: 906px;
    height: 1200px;
    background: var(--board-white);
    font-family: "Roboto", Arial, sans-serif;
    color: var(--ink);
  }
  .floral-panel {
    position: absolute;
    left: 14px;
    top: 124px;
    width: 390px;
    height: 1060px;
    background:
      radial-gradient(circle at 45% 20%, var(--leaf-pale) 0 12%, transparent 30%),
      radial-gradient(circle at 60% 45%, var(--leaf-bright) 0 18%, transparent 40%),
      radial-gradient(circle at 40% 80%, var(--leaf-pale) 0 12%, transparent 32%),
      linear-gradient(90deg, var(--leaf-deep) 0%, var(--leaf-bright) 70%, var(--leaf-pale) 100%);
  }
  .tagline {
    position: absolute;
    left: 411px;
    top: 150px;
    width: 481px;
    margin: 0;
    font-weight: 700;
    font-size: 44px;
    line-height: 58px;
    letter-spacing: -0.5px;
  }
  .tagline span { display: block; }
  .tagline .second-line { text-align: right; }
  .brand-name {
    position: absolute;
    left: 411px;
    top: 470px;
    width: 454px;
    margin: 0;
    text-align: center;
    font-weight: 400;
    font-size: 36px;
    line-height: 44px;
    color: var(--ink);
  }
  .services {
    position: absolute;
    left: 411px;
    top: 668px;
    width: 454px;
    margin: 0;
    padding: 0;
    list-style: none;
    text-align: center;
    font-weight: 400;
    font-size: 76px;
    line-height: 98px;
  }
  .web-address {
    position: absolute;
    left: 411px;
    top: 1088px;
    width: 440px;
    margin: 0;
    font-weight: 400;
    font-size: 33px;
    letter-spacing: 0.3px;
  }
</style>
</head>
<body>
  <main class="board">
    <div class="floral-panel" role="img" aria-label="Illustration of green and white stylised flowers with paint splatter, running down the left side of the board"></div>

    <h1 class="tagline">
      <span class="first-line">Flowers make</span>
      <span class="second-line">people happy</span>
    </h1>

    <p class="brand-name">Odette Marsh Petals</p>

    <ul class="services">
      <li>Flowers</li>
      <li>Weddings</li>
      <li>Giftware</li>
      <li>Workshops</li>
    </ul>

    <p class="web-address">odettemarshpetals.co.nz</p>
  </main>
</body>
</html>
```